Professional Consulting Firm Business Card Design

We need a business card design for a new professional consulting firm that specializes in petroleum, health, and financial consulting. We need a design that is trendy but elegant, and one that would make a summit 300 executive feel comfortable using our services. I have attached a logo that needs to be used in the design. I have also attached a photo of a card design that I like.

On the card we need a place for employee name, title, email address, fax number, phone number, mailing address, and website address.

Industry/Entity Type

Financial

Contact Information for Business Card

see attached

Other font styles liked:
• Calibri or your choice

Requirements
Must have
• style
Nice to have
• texture, rounded edges
Should not have
• no solid black cards but black may be used

```html
<!DOCTYPE html>
<html lang="en">
<head>
<meta charset="utf-8">
<title>Kestrel Advisory – Business Cards</title>
<link href="https://fonts.googleapis.com/css2?family=Open+Sans:wght@400;600&display=swap" rel="stylesheet">
<style>
  :root {
    --backdrop: #d9d6d2;
    --card: #1c1c1e;
    --card-edge: #2a2a2c;
    --brand-blue: #2a6fb5;
    --text-light: #f2f2f2;
    --text-silver: #c9c9cc;
    --divider: #4a4a4d;
  }
  * { box-sizing: border-box; margin: 0; padding: 0; }
  html, body {
    width: 1200px; height: 844px; overflow: hidden;
    background: var(--backdrop);
    font-family: "Open Sans", Calibri, sans-serif;
  }
  .stage {
    width: 1200px; height: 844px;
    display: flex; align-items: center; justify-content: center; gap: 60px;
  }
  .card {
    position: relative;
    width: 525px; height: 300px;
    border-radius: 10px;
    background: radial-gradient(ellipse at 30% 20%, var(--card-edge), var(--card) 70%);
    box-shadow: 0 10px 28px rgba(0,0,0,.28);
    overflow: hidden;
  }
  .brand-name {
    font-weight: 400;
    letter-spacing: 1px;
    white-space: nowrap;
  }
  /* Front face */
  .card-front .brand {
    position: absolute; top: 40px; left: 0; right: 0;
    display: flex; justify-content: center; align-items: center; gap: 10px;
  }
  .card-front .brand-mark {
    width: 14px; height: 14px; background: var(--brand-blue);
  }
  .card-front .brand-name { color: var(--brand-blue); font-size: 30px; }
  .identity {
    position: absolute; top: 150px; right: 290px;
    text-align: right; color: var(--text-light);
  }
  .person-name { color: var(--brand-blue); font-size: 22px; font-weight: 600; line-height: 1.2; }
  .person-title { font-size: 15px; margin-bottom: 14px; }
  .address { font-size: 15px; line-height: 1.35; }
  .divider {
    position: absolute; top: 150px; left: 252px;
    width: 1px; height: 110px; background: var(--divider);
  }
  .contact-list {
    position: absolute; top: 150px; left: 270px;
    list-style: none; color: var(--text-light); font-size: 15px;
  }
  .contact-list li { display: flex; align-items: center; gap: 10px; height: 26px; }
  .contact-icon {
    width: 17px; height: 17px; border-radius: 3px; background: var(--brand-blue);
    display: flex; align-items: center; justify-content: center; flex: none;
  }
  /* Back face */
  .card-back .brand {
    position: absolute; inset: 0;
    display: flex; justify-content: center; align-items: center; gap: 12px;
  }
  .card-back .brand-mark { width: 16px; height: 16px; background: var(--text-silver); }
  .card-back .brand-name { color: var(--text-silver); font-size: 34px; }
</style>
</head>
<body>
<main class="stage">
  <section class="card card-front" aria-label="Card front">
    <div class="brand">
      <span class="brand-mark"></span>
      <span class="brand-name">Kestrel Advisory</span>
    </div>
    <div class="identity">
      <p class="person-name">Daniel Avery</p>
      <p class="person-title">Managing Director</p>
      <p class="address">48 Harbor Lane, Suite 210<br>Easton, MD 21601</p>
    </div>
    <div class="divider"></div>
    <ul class="contact-list">
      <li>
        <span class="contact-icon"><svg width="11" height="11" viewBox="0 0 12 12"><path d="M3 1l2 2-1 1.5c.8 1.5 2 2.7 3.5 3.5L9 7l2 2-1.5 2C5 10.5 1.5 7 1 2.5z" fill="#fff"/></svg></span>
        (055)-318-2046
      </li>
      <li>
        <span class="contact-icon"><svg width="11" height="11" viewBox="0 0 12 12"><rect x="3" y="1" width="6" height="3" fill="#fff"/><rect x="1" y="5" width="10" height="4" fill="#fff"/><rect x="3" y="8" width="6" height="3" fill="#fff"/></svg></span>
        555-204-7731
      </li>
      <li>
        <span class="contact-icon"><svg width="11" height="11" viewBox="0 0 12 12"><rect x="1" y="3" width="10" height="7" fill="#fff"/><path d="M1 3l5 4 5-4" stroke="#2a6fb5" fill="none"/></svg></span>
        hello@kestreladvisory.com
      </li>
      <li>
        <span class="contact-icon"><svg width="11" height="11" viewBox="0 0 12 12"><path d="M5 7l2-2M4 6L2.5 7.5a1.8 1.8 0 002.5 2.5L6.5 8.5M8 6l1.5-1.5A1.8 1.8 0 007 2L5.5 3.5" stroke="#fff" stroke-width="1.5" fill="none"/></svg></span>
        www.kestreladvisory.com
      </li>
    </ul>
  </section>

  <section class="card card-back" aria-label="Card back">
    <div class="brand">
      <span class="brand-mark"></span>
      <span class="brand-name">Kestrel Advisory</span>
    </div>
  </section>
</main>
</body>
</html>
```